Roof wash and Gutter Cleaning

Would like to see our colors and logo incorporated into design along with phone number and before/after picture(s). We use a non pressure softwash process we use unlike high pressure. We are a exterior cleaning company that likes to set our standards high with safe methods to cleaning the everyday surfaces on homes.
“Serving the Tri-State Area”
A list of our services:
House washing
Shingle and metal roof washing
Deck cleaning
Window cleaning
Concrete cleaning
Gutter cleaning
415-362-0917
We do not need the address section as these will be more for our meet and greets. As well handed out as clipped door  postcards.

Target Market(s)
Shingle roof wash and gutter cleaning
Look and feel

```html
<!DOCTYPE html>
<html lang="en">
<head>
<meta charset="utf-8">
<title>Roof Wash and Gutter Cleaning Postcard</title>
<link href="https://fonts.googleapis.com/css2?family=Montserrat:wght@500;600;700;800&display=swap" rel="stylesheet">
<style>
  :root {
    --page-bg: #d4d4d4;
    --card-bg: #f3f3f3;
    --brand-blue: #3b73b4;
    --brand-green: #4bb53a;
    --ink: #1d1d1d;
    --white: #ffffff;
    --gap: #ffffff;
  }
  * { box-sizing: border-box; margin: 0; padding: 0; }
  html, body { width: 1200px; height: 900px; overflow: hidden; }
  body {
    background: var(--page-bg);
    font-family: "Montserrat", sans-serif;
    position: relative;
  }
  .postcard {
    position: absolute;
    left: 60px; top: 90px;
    width: 1080px; height: 720px;
    background: var(--card-bg);
    overflow: hidden;
  }
  .info-panel {
    position: absolute;
    left: 0; top: 0;
    width: 340px; height: 720px;
    background: var(--card-bg);
  }
  .brand {
    position: absolute;
    left: 40px; top: 46px;
    display: flex; align-items: center; gap: 12px;
  }
  .brand-dot {
    width: 34px; height: 34px; border-radius: 50%;
    background: var(--brand-blue);
    flex: none;
  }
  .brand-name {
    font-weight: 700; font-size: 17px; line-height: 1.25;
    color: var(--brand-blue);
    width: 220px;
  }
  .tagline-band {
    position: absolute;
    left: 0; top: 150px;
    width: 360px; height: 118px;
    background: var(--brand-green);
    color: var(--white);
    font-weight: 800; font-size: 30px; line-height: 1.15;
    padding: 22px 0 0 40px;
    z-index: 2;
  }
  .services-title {
    position: absolute;
    left: 40px; top: 292px;
    font-weight: 800; font-size: 21px;
    color: var(--brand-blue);
    letter-spacing: 0.5px;
  }
  .service-list {
    position: absolute;
    left: 40px; top: 330px;
    list-style: none;
  }
  .service-item {
    display: flex; align-items: center; gap: 14px;
    height: 50px;
    font-weight: 500; font-size: 17px; line-height: 1.15;
    color: var(--ink);
  }
  .service-icon {
    width: 40px; height: 40px; border-radius: 50%;
    background: var(--brand-blue);
    border: 3px solid var(--brand-green);
    box-shadow: inset 0 0 0 2px var(--white);
    display: flex; align-items: center; justify-content: center;
    flex: none;
  }
  .service-icon svg { width: 20px; height: 20px; }
  .call-band {
    position: absolute;
    left: 0; bottom: 0;
    width: 560px; height: 66px;
    background: var(--brand-blue);
    color: var(--white);
    display: flex; align-items: center; gap: 16px;
    padding-left: 40px;
    font-weight: 800; font-size: 26px;
    z-index: 3;
  }
  .call-band .phone-icon {
    width: 30px; height: 30px; border: 2px solid var(--white); border-radius: 50%;
    display: flex; align-items: center; justify-content: center;
  }
  .call-band .call-number { font-weight: 700; }
  .gallery {
    position: absolute;
    left: 340px; top: 0;
    width: 740px; height: 720px;
    display: grid;
    grid-template-columns: repeat(4, 1fr);
    grid-template-rows: 250px 220px 1fr;
    gap: 5px;
    background: var(--gap);
  }
  .photo {
    position: relative;
  }
  .photo-label {
    position: absolute;
    top: 10px; right: 14px;
    color: var(--white);
    font-weight: 600; font-size: 14px;
    text-shadow: 0 1px 2px rgba(0,0,0,0.4);
  }
  .photo--wide { grid-column: span 2; }
  .roof-before { background: linear-gradient(160deg, #7c7a62 0%, #6d6a60 40%, #8a857a 100%); }
  .roof-after  { background: linear-gradient(160deg, #6f6a55 0%, #8e8b84 45%, #a29f99 100%); }
  .tile-before { background: linear-gradient(150deg, #6d6a55 0%, #9a6a55 40%, #8a7565 100%); }
  .tile-after  { background: linear-gradient(150deg, #8d8a80 0%, #a56a55 35%, #b0705a 100%); }
  .gutter-before { background: linear-gradient(150deg, #8a8d93 0%, #6b5a45 50%, #3e3a30 100%); }
  .gutter-after  { background: linear-gradient(150deg, #6e7077 0%, #8b6a4d 50%, #c8c4a5 100%); }
  .house-before { background: linear-gradient(180deg, #b8bcc2 0%, #8a7a64 45%, #e2d9b6 70%, #4d5a38 100%); }
  .house-after  { background: linear-gradient(180deg, #c6c9cc 0%, #8c735a 45%, #e6ddba 70%, #55633c 100%); }
</style>
</head>
<body>
  <main class="postcard">
    <section class="info-panel">
      <div class="brand">
        <span class="brand-dot"></span>
        <span class="brand-name">Crestline Exterior Cleaning Co.</span>
      </div>

      <div class="tagline-band">Serving the<br>Tri-State Area</div>

      <h2 class="services-title">OUR SERVICES:</h2>
      <ul class="service-list">
        <li class="service-item">
          <span class="service-icon"><svg viewBox="0 0 20 20" fill="none" stroke="#fff" stroke-width="1.6"><path d="M3 10 10 4l7 6M5 9v7h10V9"/><rect x="8.5" y="12" width="3" height="4"/></svg></span>
          House washing
        </li>
        <li class="service-item">
          <span class="service-icon"><svg viewBox="0 0 20 20" fill="none" stroke="#fff" stroke-width="1.6"><path d="M2 14 6 6h8l4 8zM6 6l-1 8M10 6v8M14 6l1 8M4 10h12"/></svg></span>
          Shingle and metal<br>roof washing
        </li>
        <li class="service-item">
          <span class="service-icon"><svg viewBox="0 0 20 20" fill="none" stroke="#fff" stroke-width="1.6"><path d="M2 12h16M3 12v5M17 12v5M7 12v5M13 12v5M4 12V8h12v4"/></svg></span>
          Deck cleaning
        </li>
        <li class="service-item">
          <span class="service-icon"><svg viewBox="0 0 20 20" fill="none" stroke="#fff" stroke-width="1.6"><rect x="3" y="3" width="14" height="14"/><path d="M10 3v14M3 10h14"/></svg></span>
          Window cleaning
        </li>
        <li class="service-item">
          <span class="service-icon"><svg viewBox="0 0 20 20" fill="none" stroke="#fff" stroke-width="1.6"><path d="M2 16h16M4 16l2-6h8l2 6M8 10V5h4v5"/></svg></span>
          Concrete cleaning
        </li>
        <li class="service-item">
          <span class="service-icon"><svg viewBox="0 0 20 20" fill="none" stroke="#fff" stroke-width="1.6"><path d="M2 7h16v3a3 3 0 0 1-3 3H5a3 3 0 0 1-3-3zM14 13v5"/></svg></span>
          Gutter cleaning
        </li>
      </ul>
    </section>

    <section class="gallery">
      <div class="photo photo--wide roof-before" role="img" aria-label="Shingle roof covered in leaves and moss before washing"><span class="photo-label">Before</span></div>
      <div class="photo photo--wide roof-after" role="img" aria-label="Clean shingle roof after soft washing"><span class="photo-label">After</span></div>

      <div class="photo tile-before" role="img" aria-label="Red shingle roof valley filled with debris before cleaning"><span class="photo-label">Before</span></div>
      <div class="photo tile-after" role="img" aria-label="Red shingle roof valley after cleaning"><span class="photo-label">After</span></div>
      <div class="photo gutter-before" role="img" aria-label="Gutter packed with leaves before cleaning"><span class="photo-label">Before</span></div>
      <div class="photo gutter-after" role="img" aria-label="Clear gutter after cleaning"><span class="photo-label">After</span></div>

      <div class="photo photo--wide house-before" role="img" aria-label="Two-story house with stained roof before washing"><span class="photo-label">Before</span></div>
      <div class="photo photo--wide house-after" role="img" aria-label="Same two-story house with clean roof after washing"><span class="photo-label">After</span></div>
    </section>

    <div class="call-band">
      <span>CALL US</span>
      <span class="phone-icon"><svg width="16" height="16" viewBox="0 0 24 24" fill="#fff"><path d="M6.6 10.8a15.1 15.1 0 0 0 6.6 6.6l2.2-2.2a1 1 0 0 1 1-.25 11.4 11.4 0 0 0 3.6.57 1 1 0 0 1 1 1V20a1 1 0 0 1-1 1A17 17 0 0 1 3 4a1 1 0 0 1 1-1h3.5a1 1 0 0 1 1 1c0 1.25.2 2.45.57 3.57a1 1 0 0 1-.25 1z"/></svg></span>
      <span class="call-number">(415) 362-0917</span>
    </div>
  </main>
</body>
</html>
```